Modern Business Card For A Digital Advertising Company

I'll be print on the Tarn Prints Velour paper http://us.tarnprints.example/products/velour/business-cards.html
Need's to be modern and use the color palette of the logo or gray scales. I think integrating the pixelation of the logo in to the card and having it wrap from one side to the other could be interesting. My company provides ad operations, web development, and number of other services to websites around the world. You can see my website at http://www.pixelharbor.example
Contact info on the card needs to have
Dana Welloby
President
p.555.318.4406
dana@pixelharbor.example
http://www.pixelharbor.example
Doesn't necessarily need to be in that order
Target Market(s)
Website owners
Industry/Entity Type
Business
Look and feel

```html
<!DOCTYPE html>
<html lang="en">
<head>
<meta charset="utf-8">
<title>Pixel Harbor – Business Card</title>
<link rel="stylesheet" href="https://fonts.googleapis.com/css2?family=Arimo:ital,wght@0,700;1,400&family=Open+Sans:wght@600&display=swap">
<style>
  :root {
    --page-bg: #c9c9c9;
    --card-white: #ffffff;
    --gray-light: #e4e4e4;
    --gray-mid: #a3a3a3;
    --gray-dark: #4a4a4a;
    --ink: #111111;
    --brand-green: #8cc63f;
  }
  html, body {
    margin: 0;
    padding: 0;
    width: 1200px;
    height: 911px;
    overflow: hidden;
    background: var(--page-bg);
  }
  .business-card {
    position: absolute;
    left: 74px;
    top: 119px;
    width: 1049px;
    height: 613px;
    display: block;
  }
  .title-label { font-family: "Arimo", Arial, sans-serif; font-style: italic; font-weight: 400; fill: var(--ink); }
  .person-name { font-family: "Arimo", Arial, sans-serif; font-weight: 700; fill: var(--ink); letter-spacing: -1px; }
  .contact-phone { font-family: "Open Sans", sans-serif; font-weight: 600; fill: var(--ink); }
  .contact-line { font-family: "Open Sans", sans-serif; font-weight: 600; fill: var(--ink); }
  .brand-name { font-family: "Open Sans", sans-serif; font-weight: 600; fill: var(--brand-green); }
</style>
</head>
<body>
<svg class="business-card" viewBox="0 0 811 474" xmlns="http://www.w3.org/2000/svg" role="img" aria-label="Business card for Dana Welloby, President, Pixel Harbor">
  <defs>
    <linearGradient id="card-base" x1="0" y1="0" x2="0" y2="1">
      <stop offset="0" stop-color="#8f8f8f"/>
      <stop offset="0.5" stop-color="#d6d6d6"/>
      <stop offset="1" stop-color="#f2f2f2"/>
    </linearGradient>
    <linearGradient id="left-fade" x1="0" y1="0" x2="1" y2="0">
      <stop offset="0" stop-color="#9a9a9a"/>
      <stop offset="0.55" stop-color="#d8d8d8"/>
      <stop offset="1" stop-color="#ffffff" stop-opacity="0"/>
    </linearGradient>
    <linearGradient id="stripe-fade" x1="0" y1="0" x2="1" y2="0">
      <stop offset="0" stop-color="#ffffff" stop-opacity="0.9"/>
      <stop offset="1" stop-color="#ffffff" stop-opacity="0"/>
    </linearGradient>
    <linearGradient id="bottom-band" x1="0" y1="0" x2="1" y2="0">
      <stop offset="0" stop-color="#f4f4f4"/>
      <stop offset="0.3" stop-color="#ffffff"/>
      <stop offset="0.65" stop-color="#bdbdbd"/>
      <stop offset="1" stop-color="#505050"/>
    </linearGradient>
    <linearGradient id="tab-fill" x1="0" y1="0" x2="0" y2="1">
      <stop offset="0" stop-color="#f0f0f0"/>
      <stop offset="1" stop-color="#bdbdbd"/>
    </linearGradient>
    <linearGradient id="reflection-fade" x1="0" y1="0" x2="0" y2="1">
      <stop offset="0" stop-color="#000" stop-opacity="0.35"/>
      <stop offset="1" stop-color="#000" stop-opacity="0"/>
    </linearGradient>
  </defs>

  <!-- card base -->
  <rect class="card-base" x="0" y="0" width="811" height="474" fill="url(#card-base)"/>

  <!-- white face with curled right edge -->
  <path class="card-face" d="M0,38 H678 Q713,40 713,92 V300 Q716,440 811,474 H0 Z" fill="var(--card-white)"/>

  <!-- left gray fade behind name and contact rows -->
  <rect class="info-panel" x="0" y="38" width="290" height="244" fill="url(#left-fade)"/>
  <g class="row-dividers">
    <rect x="0" y="140" width="260" height="4" fill="url(#stripe-fade)"/>
    <rect x="0" y="186" width="260" height="4" fill="url(#stripe-fade)"/>
    <rect x="0" y="232" width="260" height="4" fill="url(#stripe-fade)"/>
  </g>

  <!-- title tab -->
  <path class="title-tab" d="M0,52 H118 Q132,52 132,70 Q132,88 118,88 H0 Z" fill="url(#tab-fill)"/>
  <path d="M118,52 Q132,52 132,70 Q132,88 118,88" fill="none" stroke="#6d6d6d" stroke-width="2"/>
  <text class="title-label" x="8" y="78" font-size="21">President</text>

  <!-- name and reflection -->
  <text class="person-name" x="134" y="86" font-size="40">Dana Welloby</text>
  <g aria-hidden="true" transform="translate(0,174) scale(1,-1)">
    <text class="person-name" x="134" y="86" font-size="40" fill="#000" opacity="0.22">Dana Welloby</text>
  </g>
  <rect x="130" y="90" width="260" height="34" fill="#fff" opacity="0.55"/>

  <!-- contact rows -->
  <g class="contact-phone-row">
    <circle cx="150" cy="166" r="18" fill="#777"/>
    <circle cx="150" cy="166" r="15.5" fill="var(--ink)"/>
    <rect x="143" y="155" width="14" height="23" rx="2.5" fill="none" stroke="#fff" stroke-width="2"/>
    <rect x="146" y="159" width="8" height="12" fill="#fff"/>
    <text class="contact-phone" x="179" y="177" font-size="29">555.318.4406</text>
  </g>
  <g class="contact-email-row">
    <circle cx="150" cy="213" r="18" fill="#777"/>
    <circle cx="150" cy="213" r="15.5" fill="var(--ink)"/>
    <text x="150" y="222" font-family="Arimo, Arial, sans-serif" font-weight="700" font-size="24" fill="#fff" text-anchor="middle">@</text>
    <text class="contact-line" x="182" y="220" font-size="18">dana@pixelharbor.example</text>
  </g>
  <g class="contact-web-row">
    <circle cx="150" cy="259" r="18" fill="#777"/>
    <circle cx="150" cy="259" r="15.5" fill="var(--ink)"/>
    <circle cx="151" cy="250" r="2.6" fill="#fff"/>
    <rect x="148.5" y="255" width="5" height="13" fill="#fff"/>
    <ellipse cx="150" cy="261" rx="11" ry="4" fill="none" stroke="#fff" stroke-width="1.5" transform="rotate(-25 150 261)"/>
    <text class="contact-line" x="179" y="266" font-size="18">www.pixelharbor.example</text>
  </g>

  <!-- brand name in place of the mark -->
  <g class="brand-block">
    <rect x="568" y="90" width="58" height="58" fill="var(--brand-green)"/>
    <text class="brand-name" x="597" y="212" font-size="38" text-anchor="middle">PIXEL</text>
    <text class="brand-name" x="597" y="256" font-size="38" text-anchor="middle">HARBOR</text>
  </g>

  <!-- black rule -->
  <rect class="divider-bar" x="0" y="318" width="713" height="16" fill="var(--ink)"/>

  <!-- lower gradient band -->
  <path class="lower-band" d="M0,336 H712 Q704,432 790,474 H0 Z" fill="url(#bottom-band)"/>
</svg>
</body>
</html>
```